6"x11" Postcard for Real Estate Broker

I am looking for a double sided 6"x11" (154.2mm x 279.4) with 1/16" bleed edges. This postcard will be going to print, so extremely high quality is necessary. I DO NOT want a space for mailing/address. The back side of the postcard should have information like the front.

Ideally i'm looking for a designed that knows the Western real estate market and has experience designing real estate postcards

I have uploaded several different logos for potential use. I am open to any questions or ideas. I really want it to be something that gets noticed, so i'm okay with a bold design.

If you have questions, please email me at jordan@jordanmelbeck.ca.

Target Market(s)

Middle class homes in a city of 120k people. Not targeting the luxury market

Industry/Entity Type

Real Estate Agent

Font styles to use
Serif
Sans Serif

Requirements
Must have
• - Jordan Melbeck
• - Real Estate Broker
• - Harlow Crest Realty Brokerage Inc
• - "Independently owned and operated" - This should be underneath the Harlow Crest Logo
• - www.jordanmelbeck.ca
• - Direct: 519-384-9062
• - jordan@jordanmelbeck.ca
• - something along the lines of "thinking about selling? Contact me (flexible about language used)
• - Ideally include the 2015,2016 Summit award logos upload, but if both don't fit, use the 2016 one.
• - Slogan "Your Key to Brantford Real Estate"
• - Headshot either on the front or back of postcard.
Nice to have
• - "Custom marketing plan to ensure you get the highest price"
• - "Professional photography that shows your home at its best"
• - "Video tour showcasing your homes best features"
• - "Award-winning Real Estate Broker"

```html
<!DOCTYPE html>
<html lang="en">
<head>
<meta charset="utf-8">
<title>Jordan Melbeck – Real Estate Postcard</title>
<link rel="stylesheet" href="https://fonts.googleapis.com/css2?family=Titillium+Web:wght@600;700&family=Open+Sans:wght@400;600&display=swap">
<style>
  :root{
    --red:#e31e26;
    --red-deep:#a5192a;
    --red-tab:#86131d;
    --ink:#1d1d1b;
    --panel:#efefef;
    --strip:#e4e4e4;
    --white:#ffffff;
    --stage:#ecebe8;
  }
  *{box-sizing:border-box;margin:0;padding:0}
  html,body{width:1200px;height:1126px;overflow:hidden;background:var(--stage)}
  body{position:relative;font-family:"Open Sans",Arial,sans-serif;color:var(--ink)}
  .postcard{position:absolute;left:286px;width:792px;height:437px;background:var(--white);overflow:hidden;box-shadow:0 4px 14px rgba(0,0,0,.25)}
  .postcard--front{top:103px}
  .postcard--back{top:589px}
  .postcard__shapes{position:absolute;inset:0;width:792px;height:437px}
  .abs{position:absolute}
  .heading{font-family:"Titillium Web",Arial,sans-serif;font-weight:700}
  .brand{left:22px;top:28px;width:180px;text-align:center}
  .brand__name{font-family:"Titillium Web",Arial,sans-serif;font-weight:700;font-size:30px;line-height:1;color:var(--ink);white-space:nowrap}
  .brand__sub{font-family:"Titillium Web",Arial,sans-serif;font-weight:700;font-size:15px;color:var(--ink);margin-top:20px;line-height:1.1;white-space:nowrap}
  .brand__note{font-family:"Titillium Web",Arial,sans-serif;font-weight:600;font-size:11px;color:var(--red);margin-top:12px;white-space:nowrap}
  .photo{position:absolute}
  .photo--front{left:0;top:150px;width:230px;height:215px;background:linear-gradient(180deg,#eef0f2 0%,#d9d3c6 45%,#8d9a74 80%,#4f6b33 100%)}
  .photo--back{left:0;top:0;width:345px;height:357px;background:linear-gradient(180deg,#9fc3e4 0%,#d6e3ee 30%,#c9baa0 55%,#a99680 75%,#7c9a4e 100%)}
  .headshot{left:525px;top:25px;width:267px;height:332px;background:linear-gradient(180deg,#e9e9e9 0%,#d7c4b3 35%,#2c3036 62%,#1b1e23 100%)}
  .slogan{left:225px;top:34px;width:360px;text-align:center;font-size:24px;line-height:30px}
  .agent{left:215px;top:128px;width:360px;text-align:center;color:var(--white)}
  .agent__name{font-size:31px;line-height:36px;white-space:nowrap}
  .agent__title{font-size:15px;margin-top:2px}
  .hook{left:215px;top:236px;width:330px;text-align:center;color:var(--red);font-size:36px;line-height:46px}
  .social{left:31px;top:389px;display:flex;gap:4px}
  .social__chip{width:33px;height:32px;border-radius:3px;background:#3b6aa0}
  .contact__item{position:absolute;top:389px;height:32px;display:flex;align-items:center;gap:6px;color:var(--white);font-size:16.5px;white-space:nowrap}
  .contact__item svg{width:17px;height:17px;flex:none}
  .contact__item--mail{left:204px}
  .contact__item--phone{left:448px}
  .contact__item--web{left:604px}
  .band-title{left:358px;top:80px;color:var(--white);font-size:23px;line-height:30px;white-space:nowrap}
  .benefits{left:356px;top:158px;list-style:none;font-size:14px;line-height:24.5px}
  .benefits li{display:flex;align-items:center;gap:10px;white-space:nowrap}
  .benefits svg{width:13px;height:13px;flex:none}
  .award{left:486px;top:262px;width:96px;height:86px}
  .canadian{left:612px;top:240px;width:178px;height:108px}
  .canadian__text{left:640px;top:268px;color:var(--white);font-size:30px;line-height:30px;transform:scaleX(.82);transform-origin:left;white-space:nowrap}
</style>
</head>
<body>

<section class="postcard postcard--front">
  <svg class="postcard__shapes" viewBox="0 0 792 437" aria-hidden="true">
    <rect width="792" height="437" fill="#fff"/>
  </svg>
  <div class="photo photo--front" role="img" aria-label="Photo of a two-storey suburban house with trees and lawn"></div>
  <svg class="postcard__shapes" viewBox="0 0 792 437" aria-hidden="true">
    <defs>
      <linearGradient id="redFront" x1="0" x2="1"><stop offset="0" stop-color="#e31e26"/><stop offset="1" stop-color="#a5192a"/></linearGradient>
    </defs>
    <path d="M270 0H792V357H225C200 300 205 200 212 120C220 60 240 20 270 0Z" fill="#efefef"/>
    <polygon points="215,118 792,118 792,202 182,202" fill="url(#redFront)"/>
    <polygon points="182,202 205,202 205,225" fill="#86131d"/>
  </svg>
  <div class="abs headshot" role="img" aria-label="Headshot of Jordan Melbeck in a dark suit and blue tie"></div>
  <svg class="postcard__shapes" viewBox="0 0 792 437" aria-hidden="true">
    <defs>
      <linearGradient id="redFront2" x1="0" x2="1"><stop offset="0" stop-color="#e31e26"/><stop offset="1" stop-color="#a5192a"/></linearGradient>
    </defs>
    <rect x="0" y="365" width="792" height="72" fill="#e4e4e4"/>
    <polygon points="178,357 792,357 792,437 197,437" fill="url(#redFront2)"/>
  </svg>

  <div class="abs brand">
    <div class="brand__name">Harlow Crest</div>
    <div class="brand__sub">Realty Brokerage Inc.</div>
    <div class="brand__note">Independently Owned &amp; Operated</div>
  </div>

  <h2 class="abs slogan heading">YOUR KEY TO<br>BRANTFORD REAL ESTATE</h2>
  <div class="abs agent">
    <h1 class="agent__name heading">JORDAN MELBECK</h1>
    <p class="agent__title">Real Estate Broker</p>
  </div>
  <p class="abs hook heading">THINKING ABOUT<br>SELLING?</p>

  <div class="abs social" aria-label="Social profiles"><span class="social__chip"></span><span class="social__chip"></span><span class="social__chip"></span></div>
  <span class="contact__item contact__item--mail"><svg viewBox="0 0 18 18"><circle cx="9" cy="9" r="8" fill="none" stroke="#fff" stroke-width="1.5"/><rect x="4.5" y="6" width="9" height="6" fill="#fff"/><path d="M4.5 6L9 9.5L13.5 6" stroke="#c41d28" fill="none"/></svg>jordan@jordanmelbeck.ca</span>
  <span class="contact__item contact__item--phone"><svg viewBox="0 0 18 18"><circle cx="9" cy="9" r="8" fill="none" stroke="#fff" stroke-width="1.5"/><path d="M6 5l2 2-1 1.2c.6 1.2 1.5 2.1 2.8 2.8L11 10l2 2-1.2 1.3C9 13 5 9 4.8 6.2Z" fill="#fff"/></svg>519-384-9062</span>
  <span class="contact__item contact__item--web"><svg viewBox="0 0 18 18" fill="none" stroke="#fff" stroke-width="1.2"><circle cx="9" cy="9" r="8" stroke-width="1.5"/><circle cx="9" cy="9" r="5"/><ellipse cx="9" cy="9" rx="2.2" ry="5"/><path d="M4 9h10"/></svg>jordanmelbeck.ca</span>
</section>

<section class="postcard postcard--back">
  <div class="photo photo--back" role="img" aria-label="Photo of a family home with a garage, porch and landscaped garden"></div>
  <svg class="postcard__shapes" viewBox="0 0 792 437" aria-hidden="true">
    <defs>
      <linearGradient id="redBack" x1="0" x2="1"><stop offset="0" stop-color="#e31e26"/><stop offset="1" stop-color="#a5192a"/></linearGradient>
    </defs>
    <path d="M410 0H792V357H335C330 250 330 130 345 80C360 35 380 10 410 0Z" fill="#efefef"/>
    <polygon points="320,58 792,58 792,142 305,142" fill="url(#redBack)"/>
    <polygon points="305,142 320,142 320,160" fill="#86131d"/>
    <rect x="0" y="365" width="792" height="72" fill="#e4e4e4"/>
    <polygon points="178,357 792,357 792,437 197,437" fill="url(#redBack)"/>
  </svg>

  <h2 class="abs band-title heading">YOUR KEY TO BRANTFORD REAL ESTATE</h2>
  <ul class="abs benefits">
    <li><svg viewBox="0 0 13 13"><rect width="13" height="13" rx="1" fill="#e31e26"/><path d="M3 6.5l2.5 2.5L10 3.5" stroke="#fff" stroke-width="1.8" fill="none"/></svg>Custom marketing plan to ensure you get the highest price</li>
    <li><svg viewBox="0 0 13 13"><rect width="13" height="13" rx="1" fill="#e31e26"/><path d="M3 6.5l2.5 2.5L10 3.5" stroke="#fff" stroke-width="1.8" fill="none"/></svg>Professional photography that shows your home at its best</li>
    <li><svg viewBox="0 0 13 13"><rect width="13" height="13" rx="1" fill="#e31e26"/><path d="M3 6.5l2.5 2.5L10 3.5" stroke="#fff" stroke-width="1.8" fill="none"/></svg>Video tour showcasing your homes best features</li>
    <li><svg viewBox="0 0 13 13"><rect width="13" height="13" rx="1" fill="#e31e26"/><path d="M3 6.5l2.5 2.5L10 3.5" stroke="#fff" stroke-width="1.8" fill="none"/></svg>Award-winning Real Estate Broker</li>
  </ul>

  <svg class="abs award" viewBox="0 0 96 86" role="img" aria-label="2016 Summit award badge">
    <circle cx="48" cy="40" r="38" fill="#2e3f73"/>
    <circle cx="48" cy="40" r="30" fill="#a9b0c2"/>
  </svg>
  <svg class="abs canadian" viewBox="0 0 178 108" aria-hidden="true">
    <polygon points="0,38 178,8 150,108 22,98" fill="#c41d28"/>
  </svg>
  <p class="abs canadian__text heading">100%<br>CANADIAN</p>

  <div class="abs social" aria-label="Social profiles"><span class="social__chip"></span><span class="social__chip"></span><span class="social__chip"></span></div>
  <span class="contact__item contact__item--mail"><svg viewBox="0 0 18 18"><circle cx="9" cy="9" r="8" fill="none" stroke="#fff" stroke-width="1.5"/><rect x="4.5" y="6" width="9" height="6" fill="#fff"/><path d="M4.5 6L9 9.5L13.5 6" stroke="#c41d28" fill="none"/></svg>jordan@jordanmelbeck.ca</span>
  <span class="contact__item contact__item--phone"><svg viewBox="0 0 18 18"><circle cx="9" cy="9" r="8" fill="none" stroke="#fff" stroke-width="1.5"/><path d="M6 5l2 2-1 1.2c.6 1.2 1.5 2.1 2.8 2.8L11 10l2 2-1.2 1.3C9 13 5 9 4.8 6.2Z" fill="#fff"/></svg>519-384-9062</span>
  <span class="contact__item contact__item--web"><svg viewBox="0 0 18 18" fill="none" stroke="#fff" stroke-width="1.2"><circle cx="9" cy="9" r="8" stroke-width="1.5"/><circle cx="9" cy="9" r="5"/><ellipse cx="9" cy="9" rx="2.2" ry="5"/><path d="M4 9h10"/></svg>jordanmelbeck.ca</span>
</section>

</body>
</html>
```